Asset tracing and investigation firm requires marketing brochure for services

We need a professional looking brochure with layout that supports the text that we have already drafted, is easy on the eye and can easily be navigated by clients either electronic/screen format or printed format. The wording is not finalised and all aspects need to be remain editable (including the logo and picture(s)) - preferably in Word or similarly accessible format.

```html
<!DOCTYPE html>
<html lang="en">
<head>
<meta charset="utf-8">
<title>ARVEN – Asset Tracing Services Brochure</title>
<link href="https://fonts.googleapis.com/css2?family=Montserrat:wght@400;500;600;700;800&family=Open+Sans:wght@400;600&display=swap" rel="stylesheet">
<style>
:root{
  --navy:#1b4a94;
  --navy-dark:#153d7c;
  --gold:#e6a323;
  --teal:#3b8ea5;
  --teal-light:#d7edf3;
  --grey-cell:#e3e5e8;
  --ink:#3a3a3a;
  --page:#ffffff;
  --backdrop:#e7e7e8;
  --head:'Montserrat',sans-serif;
  --body:'Open Sans',sans-serif;
}
*{box-sizing:border-box;margin:0;padding:0}
html,body{width:1200px;height:2383px;overflow:hidden}
body{background:var(--backdrop);font-family:var(--body);color:var(--ink)}
.sheet{width:1200px;height:2383px;display:flex;flex-direction:column;justify-content:space-evenly;align-items:center}
.spread{width:1140px;height:580px;background:var(--page);display:flex;box-shadow:0 2px 8px rgba(0,0,0,.12);position:relative}
.page{width:570px;height:580px;position:relative;padding:28px 30px 0}
.spread.inner{border-top:4px solid var(--gold)}

/* brand name */
.brand{font-family:var(--head);font-weight:700;color:var(--navy);display:flex;align-items:center;gap:6px;letter-spacing:1px;white-space:nowrap}
.brand .dot{width:10px;height:10px;background:var(--gold)}
.brand.light{color:#fff}

/* footer */
.page-foot{position:absolute;left:30px;right:30px;bottom:22px;display:flex;justify-content:space-between;align-items:center}
.page-foot .brand{font-size:22px}
.foot-tab{display:flex;align-items:center}
.foot-tab .url{background:var(--navy);color:#fff;font-size:10px;padding:4px 14px 4px 22px;clip-path:polygon(14px 0,100% 0,100% 100%,0 100%)}
.foot-tab .num{width:22px;height:22px;border-radius:50%;border:2px solid var(--gold);background:#fff;font-size:9px;display:flex;align-items:center;justify-content:center;margin-left:-4px;font-family:var(--head);font-weight:600;color:var(--ink)}

/* cover */
.cover-back{width:665px;background:var(--navy);color:#fff;padding:0 30px 34px;display:flex;align-items:flex-end;gap:18px;background-image:linear-gradient(135deg,#1f55a6 0%,#163f80 100%)}
.cover-back .brand{font-size:36px;padding-right:18px;border-right:1px solid rgba(255,255,255,.6)}
.contact{font-size:9px;display:grid;gap:8px}
.contact .phone{font-family:var(--head);font-weight:600;font-size:24px}
.contact-row{display:flex;align-items:center;gap:7px;white-space:nowrap}
.contact-row svg{flex:none}
.contact-col{display:grid;gap:10px;margin-left:auto;padding-bottom:4px}
.cover-front{flex:1;padding:26px 24px 0 0;position:relative}
.cover-front .photo{height:420px;margin-left:-58px;border:3px solid #fff;box-shadow:0 0 0 1px #ccd}
.cover-title{display:flex;align-items:center;gap:12px;margin-top:22px;margin-left:8px}
.cover-title .brand{font-size:26px;padding-right:12px;border-right:1px solid var(--navy)}
.cover-title h1{font-family:var(--head);font-weight:800;font-size:19px;color:var(--navy);letter-spacing:.2px;white-space:nowrap}
.cover-title h1 span{color:var(--gold)}
.cover-title p{font-size:12px;color:var(--ink);margin-top:4px;letter-spacing:.5px}

.photo{background:linear-gradient(160deg,#9aa3ad 0%,#4f6f9e 45%,#2f4e7d 70%,#6b7378 100%)}
.photo.people{background:linear-gradient(170deg,#c9ccd0 0%,#8d7a66 45%,#3b3c44 75%,#2a2b30 100%)}
.photo.portrait{background:linear-gradient(180deg,#dde1e6 0%,#b8a89a 45%,#33363d 100%)}

/* sections */
.section{margin-bottom:14px}
.sec-head{display:flex;align-items:center;margin-bottom:8px}
.sec-icon{width:30px;height:30px;border-radius:50%;border:2px solid var(--gold);background:#fff;display:flex;align-items:center;justify-content:center;position:relative;z-index:1}
.sec-label{background:var(--navy);color:#fff;font-family:var(--head);font-weight:600;font-size:12px;letter-spacing:.5px;padding:5px 34px 5px 20px;margin-left:-8px;clip-path:polygon(0 0,100% 0,calc(100% - 14px) 100%,0 100%)}
.sec-label span{color:var(--gold)}
.section p{font-size:9.6px;line-height:1.42;padding-left:40px;text-align:justify}

/* report page */
.report{display:flex;gap:18px}
.report-photo-wrap{position:relative;width:180px;flex:none;height:420px;margin-top:4px}
.report-photo-wrap::before{content:"";position:absolute;left:-6px;top:-6px;width:50px;height:50px;border-left:5px solid var(--navy);border-top:5px solid var(--navy)}
.report-photo-wrap::after{content:"";position:absolute;right:-6px;bottom:-6px;width:50px;height:50px;border-right:5px solid var(--navy);border-bottom:5px solid var(--navy)}
.report-photo-wrap .photo{position:absolute;inset:0}
.page-title{font-family:var(--head);font-weight:700;font-size:16px;color:var(--navy);margin-bottom:12px;letter-spacing:.3px;white-space:nowrap}
.page-title span{color:var(--gold)}
.report-text p{font-size:8.6px;line-height:1.38;margin-bottom:8px;text-align:justify}
.ticks{list-style:none;margin:0 0 8px}
.ticks li{display:flex;gap:8px;font-size:8.6px;line-height:1.38;margin-bottom:6px}
.ticks svg{flex:none;margin-top:1px}

/* price table */
.price-table{width:100%;border-radius:10px;overflow:hidden;border-collapse:collapse;font-size:6.4px;line-height:1.35;box-shadow:0 0 0 1px #cfd4da}
.price-table th{background:var(--navy);color:var(--gold);font-family:var(--head);font-weight:700;font-size:7px;text-align:left;padding:9px 6px;vertical-align:middle}
.price-table td{vertical-align:top;padding:7px 6px;color:#444}
.price-table td p{margin-bottom:6px}
.price-table .c1{background:var(--grey-cell)}
.price-table .c2{background:var(--teal-light)}
.price-table .c3{background:#c7e3ec}
.price-table .c4{background:#a8d2df}
.price-table .c5{background:var(--teal);color:#fff}
.price-table tr.intro td{border-bottom:1px solid #fff;height:46px}
.price-table tr.detail td{height:236px}
.price-table tr.cost td{background:#e6e7e9;font-family:var(--head);font-weight:600;font-size:11px;color:#333;padding:10px 6px;text-align:center}

/* osint */
.osint{display:flex;gap:18px}
.osint-text{flex:1}
.osint-text p{font-size:7.9px;line-height:1.38;margin-bottom:9px;text-align:justify}
.director{width:224px;flex:none;margin-top:-6px}
.director-head{background:var(--navy);color:#fff;padding:14px 16px 18px}
.director-head h3{font-family:var(--head);font-weight:500;font-size:10.5px;letter-spacing:.3px;margin-bottom:12px;white-space:nowrap}
.director-head h3 span{color:var(--gold);font-weight:700}
.director-id{display:flex;gap:12px;align-items:center}
.director-id .photo{width:64px;height:80px;border:2px solid #fff;flex:none}
.director-id strong{font-family:var(--head);font-size:11px;display:block;margin-bottom:4px}
.director-id small{font-size:7.2px;line-height:1.35;display:block;letter-spacing:.2px}
.director-body{background:var(--gold);color:#fff;padding:16px;font-size:7.4px;line-height:1.4}
.director-body p{margin-bottom:8px}
</style>
</head>
<body>
<main class="sheet">

  <section class="spread cover">
    <div class="cover-back" role="img" aria-label="Back cover: blue panel with faint city architecture texture">
      <div class="brand light"><span class="dot"></span>ARVEN</div>
      <div class="contact">
        <div class="contact-row">
          <svg width="14" height="14" viewBox="0 0 24 24"><path fill="#e6a323" d="M6.6 10.8a15 15 0 0 0 6.6 6.6l2.2-2.2a1 1 0 0 1 1-.25 11.4 11.4 0 0 0 3.6.6 1 1 0 0 1 1 1V20a1 1 0 0 1-1 1A17 17 0 0 1 3 4a1 1 0 0 1 1-1h3.5a1 1 0 0 1 1 1c0 1.25.2 2.45.6 3.6a1 1 0 0 1-.25 1z"/></svg>
          <span class="phone">0203 555 0148</span>
        </div>
        <div class="contact-row">
          <svg width="10" height="13" viewBox="0 0 20 26"><path fill="#e6a323" d="M10 0a10 10 0 0 0-10 10c0 7.5 10 16 10 16s10-8.5 10-16A10 10 0 0 0 10 0zm0 14a4 4 0 1 1 0-8 4 4 0 0 1 0 8z"/></svg>
          <span>Unit 4 Marlow Yard, 12 Fenn Street, London, EC2A 4LS</span>
        </div>
      </div>
      <div class="contact contact-col">
        <div class="contact-row">
          <svg width="12" height="9" viewBox="0 0 24 18"><rect width="24" height="18" rx="2" fill="#e6a323"/><path d="M1 2l11 8 11-8" stroke="#1b4a94" stroke-width="2" fill="none"/></svg>
          <span>enquiries@arven.co.uk</span>
        </div>
        <div class="contact-row">
          <svg width="12" height="12" viewBox="0 0 24 24"><circle cx="12" cy="12" r="10" fill="none" stroke="#e6a323" stroke-width="2"/><path d="M2 12h20M12 2c3 3 3 17 0 20M12 2c-3 3-3 17 0 20" stroke="#e6a323" stroke-width="1.6" fill="none"/></svg>
          <span>www.arven.co.uk</span>
        </div>
      </div>
    </div>
    <div class="cover-front">
      <div class="photo" role="img" aria-label="Photograph: looking up at city office towers including a curved glass skyscraper against blue sky"></div>
      <div class="cover-title">
        <div class="brand"><span class="dot"></span>ARVEN</div>
        <div>
          <h1>ASSET <span>TRACING SERVICES</span></h1>
          <p>www.arven.co.uk</p>
        </div>
      </div>
    </div>
  </section>

  <section class="spread inner">
    <div class="page">
      <div class="section">
        <div class="sec-head">
          <div class="sec-icon"><svg width="16" height="16" viewBox="0 0 24 24"><circle cx="12" cy="7" r="4" fill="none" stroke="#555" stroke-width="2"/><path d="M4 21c0-4 4-7 8-7s8 3 8 7" fill="none" stroke="#555" stroke-width="2"/></svg></div>
          <div class="sec-label">WHO <span>WE ARE</span></div>
        </div>
        <p>ARVEN are the asset tracing and investigation specialists for legal and corporate clients seeking fixed fee investigations, pre-sue and asset trace reports with fast turnarounds.</p>
      </div>
      <div class="section">
        <div class="sec-head">
          <div class="sec-icon"><svg width="16" height="16" viewBox="0 0 24 24"><rect x="4" y="5" width="16" height="16" rx="1" fill="none" stroke="#555" stroke-width="2"/><path d="M4 10h16M8 3v4M16 3v4" stroke="#555" stroke-width="2"/></svg></div>
          <div class="sec-label">WHAT <span>WE DO</span></div>
        </div>
        <p>We trace assets and gather crucial intelligence to inform your litigation strategy, bridge knowledge gaps, reduce risk and maximise recoveries. Our asset tracing and investigations services leverage advanced open source &amp; human intelligence with specialist wealth profiling techniques and detailed forensic analysis. We recognise the intricacies of medium and larger sized claims and represent maximum investigative insight and case relevance whilst keeping scope and fees proportionate to the matter in hand.</p>
      </div>
      <div class="section">
        <div class="sec-head">
          <div class="sec-icon"><svg width="16" height="16" viewBox="0 0 24 24"><rect x="3" y="4" width="18" height="16" rx="1" fill="none" stroke="#555" stroke-width="2"/><path d="M7 9h10M7 13h10M7 17h6" stroke="#555" stroke-width="2"/></svg></div>
          <div class="sec-label">CASES</div>
        </div>
        <p>We regularly conduct asset tracing and investigations on matters spanning Commercial Claims &amp; Disputes, Civil Litigation, Financial Fraud, Enforcement of an Order, Claims against a Director (including those on behalf of a Liquidator), Personal Injury, Employee Fraud, Unrepaid Loans, Investigation in respect of Bankrupt's Assets (on behalf of a Trustee), Matrimonial and Enforcement of Personal Guarantees.</p>
      </div>
      <div class="section">
        <div class="sec-head">
          <div class="sec-icon"><svg width="16" height="16" viewBox="0 0 24 24"><circle cx="12" cy="12" r="9" fill="none" stroke="#555" stroke-width="2"/><path d="M14.5 8.5a3 3 0 0 0-5 2v5M8 13h5M8 16h8" stroke="#555" stroke-width="2" fill="none"/></svg></div>
          <div class="sec-label">FEES</div>
        </div>
        <p>We urge all legal and corporate clients, where appropriate, to discuss cases with us from the inquiry stage so that we can scope out research possibilities, advise on where we can add most value and, crucially, provide a fee estimate that is both proportionate to your case and adds maximum value. We do appreciate that this is not always an option though and so, with the benefit of having worked on hundreds of cases, we have developed the following report categories under which many asset trace investigations fall.</p>
      </div>
      <footer class="page-foot">
        <div class="brand"><span class="dot"></span>ARVEN</div>
        <div class="foot-tab"><span class="url">www.arven.co.uk</span><span class="num">01</span></div>
      </footer>
    </div>

    <div class="page">
      <div class="report">
        <div class="report-photo-wrap">
          <div class="photo people" role="img" aria-label="Photograph: two business professionals reviewing a tablet together in an office"></div>
        </div>
        <div class="report-text">
          <h2 class="page-title"><span>‘LATTICE’</span> ASSET TRACE REPORTS</h2>
          <p>We have developed a suite of Asset Tracing products to suit various budgets or quantum / nature of claim. In addition to tracing specific assets, the reports seek to help clients to manage certain other risks inherent in litigation / enforcement and exploit cost effective opportunities to maximise the scope for recovery through insight and intelligence. We do that by, in varying case-specific degrees, assessing matters through the prism of Asset Tracing, Wealth Profiling, Modus Operandi and Contextual Analysis.</p>
          <p>We recognize that there is no “one size fits all” solution and we treat every case on its individual merits and requirements. Nevertheless, our intention for the information that follows is to provide a steer, at least, for costs as well as a very broad guideline for investigation in the absence of a more formal scoping exercise.</p>
          <p>With that in mind, our ‘Lattice’ Asset Tracing products meticulously piece together our findings from a myriad of sources to provide an overall picture of the subject, circumstances, and context. For relatively basic pre-sue case, for example, our remit may be to:</p>
          <ul class="ticks">
            <li><svg width="10" height="10" viewBox="0 0 20 20"><circle cx="10" cy="10" r="8.5" fill="none" stroke="#1b4a94" stroke-width="1.6"/><path d="M6 10l3 3 5-6" fill="none" stroke="#1b4a94" stroke-width="1.8"/></svg><span>Trace physical assets such as residential, investment or commercial property, holiday homes, cars and vehicles, inheritance, private limited company business interests and beneficial ownership searches</span></li>
            <li><svg width="10" height="10" viewBox="0 0 20 20"><circle cx="10" cy="10" r="8.5" fill="none" stroke="#1b4a94" stroke-width="1.6"/><path d="M6 10l3 3 5-6" fill="none" stroke="#1b4a94" stroke-width="1.8"/></svg><span>Conduct wealth profiling analysis so their lifestyle, background, family, trading history, solvency history, employment, and social media analysis</span></li>
            <li><svg width="10" height="10" viewBox="0 0 20 20"><circle cx="10" cy="10" r="8.5" fill="none" stroke="#1b4a94" stroke-width="1.6"/><path d="M6 10l3 3 5-6" fill="none" stroke="#1b4a94" stroke-width="1.8"/></svg><span>Perform solvency due diligence through judgment, bankruptcy, credit, and other proprietary database searches</span></li>
          </ul>
          <p>Beyond these basic investigations, and moving through the Lattice levels, we assist on more complex cases trace additional assets (beyond the “low hanging fruit”) and provide intelligence to bridge knowledge gaps.</p>
        </div>
      </div>
      <footer class="page-foot">
        <div class="brand"><span class="dot"></span>ARVEN</div>
        <div class="foot-tab"><span class="url">www.arven.co.uk</span><span class="num">02</span></div>
      </footer>
    </div>
  </section>

  <section class="spread">
    <div class="page">
      <h2 class="page-title"><span>‘LATTICE’</span> PRICE &amp; SERVICE GUIDE</h2>
      <table class="price-table">
        <thead>
          <tr>
            <th>PINPOINT LATTICE</th>
            <th>SNAPSHOT LATTICE</th>
            <th>FOCUSED LATTICE</th>
            <th>ENHANCED LATTICE</th>
            <th>INVESTIGATION INTERNATIONAL LATTICE</th>
          </tr>
        </thead>
        <tbody>
          <tr class="intro">
            <td class="c1">Generally recommended where the primary focus is to trace the whereabouts of the subject</td>
            <td class="c2">Generally recommended for claims of up to £80,000</td>
            <td class="c3">Generally recommended for claims of up to £250,000</td>
            <td class="c4">Generally recommended for claims in excess of £250,000</td>
            <td class="c5">Generally recommended in bespoke matters</td>
          </tr>
          <tr class="detail">
            <td class="c1"><p>Discreet address and property database enquiries</p><p>1 expert analyst</p><p>Investigation on one key subject</p><p>Email report with supporting document(s) relating to the traced residential address</p></td>
            <td class="c2"><p>Discreet tier one OSINT enquiries</p><p>2 expert analysts working on the case</p><p>Asset trace investigation on one key subject and current partner/spouse</p><p>Forensic analysis of most pertinent current corporate interest(s)</p><p>Focus points Lattice executive analysis and summary</p><p>Written report with supporting documents</p><p>Email updates on progress and key findings</p></td>
            <td class="c3"><p>Discreet tier one &amp; two OSINT enquiries</p><p>2 to 3 expert analysts working on the case</p><p>Asset trace investigation on key subject, current partner/spouse and immediate family</p><p>Forensic analysis of current corporate interest(s) and pertinent previous interest(s)</p><p>Human intelligence enquiries</p><p>Site attendance and pre-text enquiries</p><p>Focus points Lattice executive analysis and summary</p><p>Written report with supporting documents</p><p>Regular email/telephone updates on progress</p></td>
            <td class="c4"><p>Discreet tier one, two &amp; three OSINT enquiries</p><p>3+ expert analysts/investigators working on the case</p><p>Asset trace investigation on one or two key subjects, current partner/spouse, immediate family and close associates</p><p>Bank account searches (subject to data protection conditions being satisfied)</p><p>International database enquiries</p><p>Potential for multijurisdictional source enquiries</p><p>Forensic analysis of current and previous corporate interest(s)</p><p>Human intelligence enquiries</p><p>Site attendance and pre-text enquiries</p><p>Focus points Lattice executive analysis and summary</p><p>Written report with supporting documents</p><p>Enhanced report output - tabulated results &amp; charts</p><p>Regular email / telephone updates on progress</p><p>Case debrief</p></td>
            <td class="c5"><p>To be determined as per the specific scope of investigation</p></td>
          </tr>
          <tr class="cost">
            <td>£400</td><td>£500</td><td>£900</td><td>£1,500</td><td>POA</td>
          </tr>
        </tbody>
      </table>
      <footer class="page-foot">
        <div class="brand"><span class="dot"></span>ARVEN</div>
        <div class="foot-tab"><span class="url">www.arven.co.uk</span><span class="num">03</span></div>
      </footer>
    </div>

    <div class="page">
      <div class="osint">
        <div class="osint-text">
          <h2 class="page-title"><span>OSINT</span> TIERS</h2>
          <p>Tier One OSINT sources are essential public and proprietary datasets and may include: Voters Roll Records, Consensual Marketing Data Footprints, Current Active Credit File Footprints, Land Title Records, Landline, Mobile &amp; Ex-Directory (hidden) Telephone Records, Corporate Records, Other Proprietary Database Sources, Social Media, County Court Judgment Databases, High Court Judgment Databases, Bankruptcy Searches, Proprietary Database Shareholder Searches, Historical and Concurrent Credit File Footprints, House Prices Information Database Checks, Property Company Reverse Land Title Enquiries, Probate / Inheritance, Company Credit Files and Accounts Analysis, Genealogy Databases &amp; Family Searches, Interim Charging Orders / Property Charge Databases, Insurance Data Indicators, On-the-ground Enquiries, Historical Land Title Office searches, Corporate Payment Data, Risk Scores, Government Databases, Data Leaks, Postal Forwarding Database, Vehicle Finance Enquiries, International Corporate Databases, Regional News, Business Publications.</p>
          <p>Tier Two sources may sit behind paywalls, require more advanced data mining/analysis or represent more time intensive investigations such as: Deep Internet, Civil Registry enquiries, Human Intelligence / Source Enquiries, Third Party Credit Agency Enquiries, Local Language News Sources, Vehicle Finance Enquiries, Specialist Paywalled Data Repositories, Archived Domain &amp; Website Registration, Archived / Hidden Corporate Data, Archived Voters Roll Footprint Searches, Local Authority Planning Application, Self-Employment Checks.</p>
          <p>Tier Three sources, enacted by specialists in their respective fields, require individual expert manipulation, the use of technology or AI, and/or sit behind advanced paywalls. These include: Dark Web, Engagement of Advanced Machine Learning and Artificial Intelligence Algorithms, Physical Attendances, Pre-Text Enquiries, Bank Account Searches (subject to data protection conditions being satisfied), International Database Searches, In-Person Registry Searches, Physical Asset Identification, Large Data Gathering and Analysis Software.</p>
        </div>
        <aside class="director">
          <div class="director-head">
            <h3>DIRECTOR OF <span>ASSET TRACING</span></h3>
            <div class="director-id">
              <div class="photo portrait" role="img" aria-label="Portrait photograph of the director in a dark suit"></div>
              <div>
                <strong>DANIEL MARSH</strong>
                <small>OPEN SOURCE INVESTIGATIONS &amp; INTELLIGENCE SPECIALIST</small>
              </div>
            </div>
          </div>
          <div class="director-body">
            <p>Since beginning his career with Meridian Risk over 12 years ago, Daniel has honed his skills in the manipulation of open source intelligence, investigation and analysis.</p>
            <p>He specialises in intelligence-led desktop and local source forensic investigation in the context of both discrete stand-alone instructions and project implementation. As a result, our range of Lattice Asset Tracing Reports benefits from his unique skillset and vast experience of working on literally hundreds of UK and International Asset Tracing cases.</p>
            <p>As well as contentious civil litigation, pre-sue and fraud investigation, Daniel's experience also spans business intelligence, KYC / AML compliance projects and other due diligence, all of which feeds into the scope of our investigations.</p>
          </div>
        </aside>
      </div>
      <footer class="page-foot">
        <div class="brand"><span class="dot"></span>ARVEN</div>
        <div class="foot-tab"><span class="url">www.arven.co.uk</span><span class="num">04</span></div>
      </footer>
    </div>
  </section>

</main>
</body>
</html>
```